Brit Rock covers band "The Tin Kettles" requires poster for Fernhollow Club Friday March 31st

I want a design for a poster (A3 and A4) and Facebook/Instagram ads.
Primary focus is the band name logo "The Tin Kettles", style as in attached file, followed by tag "Old Skool Brit Rock".
Backdrop to be 60's psychedelic art.
Secondary focus is the venue "The Fernhollow Club"
Supporting text to include:
- 27 Quill Street, Chatswood SYDNEY
- Friday 31st March 2023
- 7:00 pm until late
- Bar sales refreshments
- NO admission fee

```html
<!DOCTYPE html>
<html lang="en">
<head>
<meta charset="utf-8">
<title>The Tin Kettles – Fernhollow Club Poster</title>
<link href="https://fonts.googleapis.com/css2?family=Abril+Fatface&family=Lilita+One&family=Roboto:wght@400;500&display=swap" rel="stylesheet">
<style>
  :root {
    --page-bg: #fdf5f5;
    --purple: #7b3fd0;
    --deep-purple: #6a2fb0;
    --magenta: #b63ce0;
    --lavender: #d9a9f2;
    --pale-lavender: #e9d6f7;
    --cyan: #4fe0cf;
    --blue: #2a5db0;
    --beige: #f0d8a8;
    --black: #000000;
    --white: #ffffff;
  }
  * { margin: 0; padding: 0; box-sizing: border-box; }
  html, body { width: 1200px; height: 1177px; overflow: hidden; background: var(--page-bg); }
  .poster {
    position: absolute; left: 276px; top: 106px; width: 679px; height: 961px;
    overflow: hidden;
  }
  .backdrop {
    position: absolute; inset: 0;
    background:
      radial-gradient(ellipse 40% 25% at 20% 10%, #f7e7b0 0%, transparent 70%),
      radial-gradient(ellipse 45% 30% at 80% 45%, #f6f0c0 0%, transparent 70%),
      radial-gradient(ellipse 50% 30% at 15% 45%, #7fd7f0 0%, transparent 70%),
      radial-gradient(ellipse 40% 30% at 75% 80%, #f2b6e6 0%, transparent 70%),
      radial-gradient(ellipse 50% 35% at 30% 75%, #9a6ef0 0%, transparent 70%),
      radial-gradient(ellipse 40% 25% at 60% 25%, #c9b8f5 0%, transparent 70%),
      linear-gradient(160deg, #b8a4f2 0%, #8fc6f3 40%, #c7a2ef 70%, #a785f0 100%);
  }
  .band-name {
    position: absolute; left: 30px; top: 34px; width: 400px;
    font-family: "Abril Fatface", serif; color: var(--white);
    font-size: 104px; line-height: 0.98; text-align: center; letter-spacing: -1px;
  }
  .admission-badge { position: absolute; left: 403px; top: -40px; width: 300px; height: 300px; }
  .tagline {
    position: absolute; left: 28px; top: 366px; width: 625px; height: 65px;
    background: var(--white); display: flex; align-items: center; justify-content: center;
    font-family: "Lilita One", sans-serif; font-size: 44px; letter-spacing: 1px;
  }
  .tagline .old-skool { color: var(--deep-purple); margin-right: 12px; }
  .tagline .brit-rock { color: var(--blue); }
  .info-panel { position: absolute; left: 28px; top: 453px; width: 456px; height: 486px; background: var(--black); }
  .pin-icon { position: absolute; left: 40px; top: 16px; width: 32px; height: 44px; }
  .venue {
    position: absolute; left: 14px; top: 62px; width: 213px; text-align: center;
    font-family: "Abril Fatface", serif; line-height: 1.1;
  }
  .venue .the, .venue .club { color: var(--white); font-size: 28px; }
  .venue .place { color: var(--lavender); font-size: 29px; display: block; }
  .venue-rule { position: absolute; left: 122px; top: 170px; width: 54px; height: 9px;
    border-top: 2px solid var(--cyan); border-bottom: 2px solid var(--cyan); }
  .address {
    position: absolute; left: 38px; top: 192px; font-family: "Roboto", sans-serif;
    font-size: 18px; line-height: 1.3; color: var(--white);
  }
  .band-photo {
    position: absolute; left: 2px; top: 294px; width: 454px; height: 192px;
    background: radial-gradient(ellipse 70% 60% at 50% 45%, #3a3650 0%, #15141c 60%, #000 100%);
  }
  .date-box {
    position: absolute; left: 271px; top: 468px; width: 195px; height: 267px;
    background: var(--purple); border: 4px solid var(--beige);
    text-align: center; font-family: "Abril Fatface", serif; line-height: 1;
    padding-top: 14px;
  }
  .date-box .day { color: var(--beige); font-size: 58px; display: block; }
  .date-box .num { color: var(--white); font-size: 86px; display: block; }
  .date-box .month { color: var(--beige); font-size: 40px; display: block; margin-top: 2px; }
  .date-box .year { color: var(--white); font-size: 40px; display: block; margin-top: 4px; }
  .time-strip {
    position: absolute; left: 427px; top: 561px; width: 226px; height: 50px;
    background: var(--black); color: var(--white); display: flex; align-items: center; justify-content: center;
    font-family: "Lilita One", sans-serif; font-size: 18px; letter-spacing: 1px;
  }
  .bar-badge { position: absolute; left: 389px; top: 743px; width: 188px; height: 188px; }
</style>
</head>
<body>
<div class="poster">
  <div class="backdrop" role="img" aria-label="Swirling 60s psychedelic marbled backdrop in lavender, blue, pink and gold"></div>

  <div class="band-name">THE TIN KETTLES</div>

  <svg class="admission-badge" viewBox="0 0 300 300" aria-label="No admission fee">
    <circle cx="150" cy="150" r="150" fill="#7b3fd0"/>
    <circle cx="150" cy="150" r="146" fill="none" stroke="#4fe0cf" stroke-width="5"/>
    <circle cx="150" cy="150" r="100" fill="#e9d6f7"/>
    <circle cx="150" cy="150" r="90" fill="#7b3fd0"/>
    <circle cx="150" cy="150" r="76" fill="#b63ce0"/>
    <g font-family="Lilita One, sans-serif" fill="#ffffff" text-anchor="middle" font-size="22" letter-spacing="1">
      <text x="150" y="130">NO</text>
      <text x="150" y="158">ADMISSION</text>
      <text x="150" y="186">FEE</text>
    </g>
  </svg>

  <div class="tagline"><span class="old-skool">OLD SKOOL</span><span class="brit-rock">BRIT ROCK</span></div>

  <div class="info-panel">
    <svg class="pin-icon" viewBox="0 0 32 44" aria-hidden="true">
      <path d="M16 0C7 0 0 7 0 16c0 11 16 28 16 28s16-17 16-28C32 7 25 0 16 0z" fill="#4fe0cf"/>
      <circle cx="16" cy="16" r="6" fill="#000"/>
    </svg>
    <div class="venue">
      <span class="the">THE</span>
      <span class="place">FERNHOLLOW</span>
      <span class="club">CLUB</span>
    </div>
    <div class="venue-rule"></div>
    <div class="address">27 Quill Street,<br>Chatswood SYDNEY</div>
    <div class="band-photo" role="img" aria-label="Moody photograph of the four band members against black"></div>
  </div>

  <div class="date-box">
    <span class="day">FRI</span>
    <span class="num">31</span>
    <span class="month">MARCH</span>
    <span class="year">2023</span>
  </div>

  <div class="time-strip">7:00 PM UNTIL LATE</div>

  <svg class="bar-badge" viewBox="0 0 188 188" aria-label="Bar sales refreshments">
    <circle cx="94" cy="94" r="94" fill="#7b3fd0"/>
    <circle cx="94" cy="94" r="84" fill="#ffffff"/>
    <circle cx="94" cy="94" r="78" fill="#4fe0cf"/>
    <g font-family="Lilita One, sans-serif" text-anchor="middle">
      <text x="94" y="82" font-size="30" fill="#6a2fb0">BAR</text>
      <text x="94" y="112" font-size="30" fill="#6a2fb0">SALES</text>
      <text x="94" y="132" font-size="14" fill="#000000">REFRESHMENTS</text>
    </g>
  </svg>
</div>
</body>
</html>
```